Carradine Advisory Cover 1 - Hunting Profit As Moggle Hunts the Flimbit

Carradine Advisory is a business consulting firm. We will publish a series of four thought leadership pieces online and via PDF. The first of the series is attached to this project. We need an eye-catching cover page with a back page that keeps with our branding. The document attached is in the final draft, and the cover and pack pages are placeholders only. You can find more about our branding and style on our website www.carradineadvisory.com.au. The other three projects can be found here with a similar brief, and you are welcome to submit a design for all 4.

```html
<!DOCTYPE html>
<html lang="en">
<head>
<meta charset="utf-8">
<title>Carradine Advisory – Hunting Profit As Moggle Hunts the Flimbit</title>
<link href="https://fonts.googleapis.com/css2?family=Poppins:wght@400;500;600;700&display=swap" rel="stylesheet">
<style>
  :root {
    --backdrop: #9d9d9d;
    --paper: #f0f1f3;
    --paper-shade: #e2e6ea;
    --ink: #2e3640;
    --orange: #f7931e;
    --blue: #00aeef;
    --white: #ffffff;
  }
  * { box-sizing: border-box; margin: 0; padding: 0; }
  html, body { width: 1200px; height: 848px; overflow: hidden; }
  body {
    background: var(--backdrop);
    font-family: "Poppins", sans-serif;
    color: var(--ink);
    position: relative;
  }
  .page {
    position: absolute;
    top: 29px;
    width: 560px;
    height: 792px;
    background: var(--paper);
    overflow: hidden;
  }
  .page--cover { left: 27px; }
  .page--back { left: 613px; }
  .page__art { position: absolute; inset: 0; width: 560px; height: 792px; }

  .brand { position: absolute; display: flex; align-items: center; }
  .brand__dot { border-radius: 50%; background: var(--blue); flex: none; }
  .brand__name { font-weight: 600; line-height: 1.05; color: var(--ink); }
  .page--cover .brand { left: 38px; top: 52px; gap: 12px; }
  .page--cover .brand__dot { width: 40px; height: 40px; }
  .page--cover .brand__name { font-size: 19px; }
  .page--back .brand { left: 40px; top: 56px; gap: 16px; }
  .page--back .brand__dot { width: 62px; height: 62px; }
  .page--back .brand__name { font-size: 29px; }

  .cover-title { position: absolute; left: 40px; top: 230px; }
  .cover-title__main { font-size: 50px; font-weight: 700; line-height: 1.1; color: var(--ink); }
  .cover-title__sub { margin-top: 10px; font-size: 29px; font-weight: 600; line-height: 1.7; color: var(--white); }

  .web-link {
    position: absolute; display: flex; align-items: center; gap: 7px;
    font-size: 14px; font-weight: 500;
  }
  .web-link svg { width: 13px; height: 13px; }
  .page--cover .web-link { left: 268px; top: 748px; color: var(--white); }
  .page--back .web-link { left: 284px; top: 748px; color: var(--ink); }

  .contact { position: absolute; left: 40px; top: 190px; width: 380px; }
  .contact__heading { font-size: 34px; font-weight: 600; color: var(--orange); line-height: 1.2; }
  .contact__intro { margin-top: 22px; font-size: 18.5px; font-weight: 600; line-height: 1.35; }
  .contact__intro strong { font-weight: 700; }
  .person { margin-top: 30px; }
  .person + .person { margin-top: 32px; }
  .person__name { font-size: 21px; font-weight: 600; color: var(--orange); line-height: 1.2; }
  .person__role { font-size: 12px; font-weight: 600; color: var(--blue); line-height: 1.3; margin-bottom: 8px; }
  .person__line { font-size: 13px; line-height: 1.4; }

  .follow { position: absolute; left: 40px; top: 750px; display: flex; align-items: center; gap: 12px; }
  .follow__label { font-size: 11.5px; font-weight: 600; }
  .follow__tile { width: 14px; height: 14px; background: var(--ink); border-radius: 2px; }
</style>
</head>
<body>

<section class="page page--cover">
  <svg class="page__art" viewBox="0 0 420 594" preserveAspectRatio="none">
    <defs>
      <linearGradient id="tone-steel" x1="0" y1="0" x2="1" y2="1">
        <stop offset="0" stop-color="#7c8794"/><stop offset="1" stop-color="#c4c9cf"/>
      </linearGradient>
      <linearGradient id="tone-amber" x1="0" y1="0" x2="1" y2="1">
        <stop offset="0" stop-color="#b8823f"/><stop offset="1" stop-color="#d9a662"/>
      </linearGradient>
      <linearGradient id="tone-sky" x1="0" y1="0" x2="1" y2="1">
        <stop offset="0" stop-color="#1c82c7"/><stop offset="1" stop-color="#0b4f86"/>
      </linearGradient>
      <linearGradient id="tone-sand" x1="0" y1="0" x2="1" y2="1">
        <stop offset="0" stop-color="#c38a44"/><stop offset="1" stop-color="#6e4a26"/>
      </linearGradient>
    </defs>
    <polygon class="stripe-blue" fill="var(--blue)" points="215,0 245,0 168,128 138,128"/>
    <g role="img" aria-label="Photo of a glass office tower seen from below">
      <polygon fill="url(#tone-steel)" points="252,0 337,0 260,128 175,128"/>
    </g>
    <g role="img" aria-label="Photo of a warm-toned stone facade">
      <polygon fill="url(#tone-amber)" points="347,0 420,0 420,128 270,128"/>
    </g>
    <polygon class="title-band" fill="var(--orange)" points="0,128 420,128 318,298 0,298"/>
    <polygon class="corner-accent" fill="var(--orange)" points="0,298 38,298 0,362"/>
    <g role="img" aria-label="Photo of blue city skyscrapers">
      <polygon fill="url(#tone-sky)" points="46,298 165,298 0,573 0,375"/>
    </g>
    <g role="img" aria-label="Photo of a businessman standing among tall stone walls">
      <polygon fill="url(#tone-sand)" points="176,298 309,298 132,594 0,594 0,591"/>
    </g>
    <polygon class="blue-field" fill="var(--blue)" points="420,140 420,594 149,594 417,140"/>
    <polygon class="shade-strip" fill="var(--paper-shade)" points="420,478 420,594 352,594"/>
  </svg>

  <div class="brand">
    <span class="brand__dot"></span>
    <span class="brand__name">Carradine<br>Advisory</span>
  </div>

  <h1 class="cover-title">
    <span class="cover-title__main">Hunting Profit</span>
    <div class="cover-title__sub">As Moggle Hunts<br>the Flimbit</div>
  </h1>

  <div class="web-link">
    <svg viewBox="0 0 16 16" fill="none" stroke="currentColor" stroke-width="1.4"><circle cx="8" cy="8" r="6.5"/><ellipse cx="8" cy="8" rx="2.8" ry="6.5"/><line x1="1.5" y1="8" x2="14.5" y2="8"/></svg>
    www.carradineadvisory.com.au
  </div>
</section>

<section class="page page--back">
  <svg class="page__art" viewBox="0 0 420 594" preserveAspectRatio="none">
    <polygon class="shade-corner" fill="var(--paper-shade)" points="0,0 130,0 0,72"/>
    <polygon class="shade-band" fill="var(--paper-shade)" points="360,0 420,0 420,40 205,594 140,594"/>
    <polygon class="orange-wedge" fill="var(--orange)" points="414,0 420,0 420,330 265,460"/>
    <polygon class="blue-field" fill="var(--blue)" points="420,318 420,594 150,594"/>
  </svg>

  <div class="brand">
    <span class="brand__dot"></span>
    <span class="brand__name">Carradine<br>Advisory</span>
  </div>

  <div class="contact">
    <h2 class="contact__heading">Contact us</h2>
    <p class="contact__intro">Find out how <strong>Carradine Advisory</strong> can help build your company into a market leader today.</p>

    <div class="person">
      <div class="person__name">Edmund Carradine</div>
      <div class="person__role">Managing Director</div>
      <div class="person__line">Mobile: +61 400 318 264</div>
      <div class="person__line">Email: edmund@carradineadvisory.com.au</div>
    </div>

    <div class="person">
      <div class="person__name">Hugo Carradine</div>
      <div class="person__role">Managing Director</div>
      <div class="person__line">Mobile: +61 400 592 107</div>
      <div class="person__line">Email: hugo@carradineadvisory.com.au</div>
    </div>
  </div>

  <div class="follow">
    <span class="follow__label">Follow us</span>
    <span class="follow__tile" aria-label="Social profile"></span>
    <span class="follow__tile" aria-label="Social profile"></span>
  </div>

  <div class="web-link">
    <svg viewBox="0 0 16 16" fill="none" stroke="currentColor" stroke-width="1.4"><circle cx="8" cy="8" r="6.5"/><ellipse cx="8" cy="8" rx="2.8" ry="6.5"/><line x1="1.5" y1="8" x2="14.5" y2="8"/></svg>
    www.carradineadvisory.com.au
  </div>
</section>

</body>
</html>
```